Occupational Therapy Clinic Advertisement

Create an advertisement for a magazine. Below I have attached my original ad (Ad 2020.pdf) . I want the ad changed and it should be eye catching. I would like a eye catching graphics added in the ad. It should be a graphic image that applies to education. I am attaching a sample graphic image of that I liked from someone elses ad- it should not be the same- it just is there to show what I like. Please use the same words from my original ad.Dimensions: 3.75in x 10.3 in

Target Market(s)

Parents of School aged children

Requirements
Must have
• Must have eye catching Graphic. Colors should be eye catching for a typed magazine.

```html
<!DOCTYPE html>
<html lang="en">
<head>
<meta charset="utf-8">
<title>Bright Path OT Services – Magazine Ad</title>
<link rel="stylesheet" href="https://fonts.googleapis.com/css2?family=Montserrat:wght@500;600;700;800&display=swap">
<style>
  :root {
    --backdrop: #2a201b;
    --orange: #ee4a24;
    --orange-text: #ee4424;
    --yellow-top: #fbb41a;
    --yellow-bottom: #fedd7a;
    --blue: #3c8fd2;
    --blue-text: #3a8ed4;
    --sky-top: #9ccaec;
    --sky-bottom: #ffffff;
    --ink: #111111;
    --white: #ffffff;
    --kid-tone: #f4a46a;
    --tree-tone: #c9d8e0;
  }
  * { box-sizing: border-box; margin: 0; padding: 0; }
  html, body { width: 1200px; height: 1200px; overflow: hidden; }
  body {
    background: var(--backdrop);
    font-family: "Montserrat", Arial, sans-serif;
    color: var(--ink);
    position: relative;
  }
  .ad {
    position: absolute;
    top: 84px;
    width: 374px;
    height: 1022px;
    overflow: hidden;
  }
  .ad--warm { left: 184px; background: linear-gradient(180deg, var(--yellow-top) 10%, var(--yellow-bottom) 75%); }
  .ad--cool { left: 672px; background: linear-gradient(180deg, var(--sky-top) 10%, var(--sky-bottom) 70%); }
  .band { position: absolute; left: 0; width: 374px; display: block; }
  .band--top { top: 0; height: 130px; }
  .band--bottom { bottom: 0; height: 280px; }
  .block { position: absolute; left: 0; width: 374px; text-align: center; }
  .title {
    top: 28px; color: var(--white); font-weight: 800; font-size: 20px; line-height: 24px;
  }
  .questions p { font-size: 17px; line-height: 27px; margin-bottom: 10px; }
  .ad--warm .questions { top: 179px; font-weight: 600; text-transform: uppercase; }
  .ad--cool .questions { top: 120px; font-weight: 500; font-size: 17.5px; }
  .promise { font-weight: 800; text-transform: uppercase; }
  .ad--warm .promise { top: 401px; color: var(--orange-text); font-size: 21.5px; line-height: 26.5px; }
  .ad--cool .promise { top: 322px; color: var(--blue-text); font-size: 22px; line-height: 31px; }
  .service { position: absolute; font-size: 15px; line-height: 24px; font-weight: 600; text-align: left; text-transform: uppercase; }
  .service strong { font-weight: 800; }
  .ad--warm .service--evaluate { left: 14px; top: 512px; }
  .ad--warm .service--deficits { left: 222px; top: 509px; }
  .ad--warm .service--methods { left: 60px; width: 232px; top: 609px; text-align: center; }
  .ad--cool .service { left: 179px; line-height: 23.5px; font-size: 15px; }
  .ad--cool .service--evaluate { top: 434px; }
  .ad--cool .service--deficits { top: 527px; }
  .ad--cool .service--methods { top: 631px; }
  .ages { font-weight: 800; }
  .ad--warm .ages { top: 690px; left: 60px; width: 232px; font-size: 17px; }
  .ad--cool .ages { top: 716px; font-size: 22px; }
  .board { font-weight: 800; font-size: 16.5px; text-transform: uppercase; }
  .ad--warm .board { top: 730px; }
  .ad--cool .board { top: 762px; }
  .contact { color: var(--white); font-weight: 500; font-size: 13.5px; line-height: 20px; text-transform: uppercase; }
  .ad--cool .contact { color: var(--ink); line-height: 21px; }
  .ad--warm .contact--location { top: 804px; }
  .ad--warm .contact--list { top: 870px; }
  .ad--warm .contact--email { top: 906px; }
  .ad--cool .contact--location { top: 808px; }
  .ad--cool .contact--list { top: 868px; }
  .ad--cool .contact--email { top: 925px; }
  .contact--email { text-transform: none; font-size: 15px; }
  .contact--email strong { font-weight: 800; }
  .therapist { font-weight: 800; font-size: 19px; }
  .ad--warm .therapist { top: 936px; color: var(--white); }
  .ad--cool .therapist { top: 957px; }
  .phone { font-weight: 800; font-size: 28px; display: flex; justify-content: center; align-items: center; gap: 6px; }
  .ad--warm .phone { top: 974px; color: var(--white); }
  .ad--cool .phone { top: 981px; }
  .phone svg { width: 24px; height: 24px; }
  .art { position: absolute; }
  .art--kid { background: radial-gradient(circle at 50% 50%, #f7b37d 0%, var(--kid-tone) 60%, rgba(244,164,106,0) 72%); border-radius: 40%; }
  .art--kid-top { left: 0; top: 120px; width: 74px; height: 90px; }
  .art--kid-side { left: 308px; top: 354px; width: 66px; height: 90px; }
  .art--kid-low { left: 0; top: 624px; width: 62px; height: 90px; }
  .art--tree { left: 0; top: 420px; width: 168px; height: 294px; border-radius: 50% 50% 10% 10%; background: radial-gradient(ellipse at 55% 35%, #f3e6c9 0%, var(--tree-tone) 55%, rgba(201,216,224,0) 78%); }
</style>
</head>
<body>

<article class="ad ad--warm">
  <svg class="band band--top" viewBox="0 0 374 130" preserveAspectRatio="none" aria-hidden="true">
    <polygon points="0,0 374,0 374,96 0,126" fill="var(--orange)"/>
  </svg>
  <svg class="band band--bottom" viewBox="0 0 374 280" preserveAspectRatio="none" aria-hidden="true">
    <polygon points="0,50 374,8 374,280 0,280" fill="var(--orange)"/>
  </svg>

  <h1 class="block title">BRIGHT PATH<br>OT SERVICES (555) 014-2288</h1>

  <div class="art art--kid art--kid-top" role="img" aria-label="Cartoon child peeking in from the left edge"></div>
  <div class="art art--kid art--kid-side" role="img" aria-label="Cartoon child peeking in from the right edge"></div>
  <div class="art art--kid art--kid-low" role="img" aria-label="Cartoon child waving from the left edge"></div>

  <div class="block questions">
    <p>Does your child struggle<br>with Reading/Kriah?</p>
    <p>Knows the information<br>but fails the test?</p>
    <p>Has difficulty remembering<br>names and dates?</p>
  </div>

  <p class="block promise">Yes your child<br>can will succeed<br>in school!</p>

  <p class="service service--evaluate"><strong>We evaluate:</strong><br>Using<br>standardized<br>evaluations</p>
  <p class="service service--deficits">We treat the<br>underlying<br>processing<br>deficits</p>
  <p class="service service--methods">We treat:<br>Using researched<br>based techniques</p>

  <p class="block ages">AGES: 6-18</p>
  <p class="block board">Board of Ed OT RSA's accepted</p>

  <p class="block contact contact--location">Located in Borough Park<br>Evaluations done in Borough Park &amp;<br>Staten Island</p>
  <p class="block contact contact--list">For more information or<br>to be added to our email list,</p>
  <p class="block contact contact--email"><strong>please email:</strong> brightpathot@example.com</p>
  <p class="block therapist">Dina Halpern OTR/L</p>
  <p class="block phone">
    <svg viewBox="0 0 24 24" aria-hidden="true"><path d="M6.6 2.5 9.4 2l1.4 4.6-2 1.4c.9 2.6 3 4.8 5.7 5.9l1.5-1.9 4.5 1.6-.6 2.9c-.2 1-1.1 1.6-2.1 1.5C10.6 17.400 5.3 12.100 4.500 4.900c-.1-1 .6-2.200 2.100-2.400z" fill="none" stroke="currentColor" stroke-width="2" stroke-linejoin="round"/></svg>
    (555)014-2288
  </p>
</article>

<article class="ad ad--cool">
  <svg class="band band--top" viewBox="0 0 374 130" preserveAspectRatio="none" aria-hidden="true">
    <path d="M0,0 H374 V84 Q187,118 0,84 Z" fill="var(--blue)"/>
  </svg>
  <svg class="band band--bottom" viewBox="0 0 374 280" preserveAspectRatio="none" aria-hidden="true">
    <path d="M0,78 Q187,38 374,78 V280 H0 Z" fill="var(--blue)"/>
  </svg>

  <h1 class="block title">BRIGHT PATH<br>OT SERVICES (555) 014-2288</h1>

  <div class="block questions">
    <p>Does your child struggle<br>with Reading/Kriah?</p>
    <p>Knows the information<br>but fails the test?</p>
    <p>Has difficulty remembering<br>names and dates?</p>
  </div>

  <p class="block promise">Yes your child<br>can will succeed<br>in school!</p>

  <div class="art art--tree" role="img" aria-label="Colourful education tree illustration with books, pencils and school words in its crown"></div>

  <p class="service service--evaluate"><strong>We evaluate:</strong><br>Using<br>standardized<br>evaluations</p>
  <p class="service service--deficits">We treat the<br>underlying<br>processing<br>deficits</p>
  <p class="service service--methods">We treat:<br>Using researched<br>based techniques</p>

  <p class="block ages">AGES: 6-18</p>
  <p class="block board">Board of Ed OT RSA's accepted</p>

  <p class="block contact contact--location">Located in Borough Park<br>Evaluations done in Borough Park &amp;<br>Staten Island</p>
  <p class="block contact contact--list">For more information or<br>to be added to our email list,</p>
  <p class="block contact contact--email"><strong>please email:</strong> brightpathot@example.com</p>
  <p class="block therapist">Dina Halpern OTR/L</p>
  <p class="block phone">
    <svg viewBox="0 0 24 24" aria-hidden="true"><path d="M6.6 2.5 9.4 2l1.4 4.6-2 1.4c.9 2.6 3 4.8 5.7 5.9l1.5-1.9 4.5 1.6-.6 2.9c-.2 1-1.1 1.6-2.1 1.5C10.6 17.400 5.3 12.100 4.500 4.900c-.1-1 .6-2.200 2.100-2.400z" fill="none" stroke="currentColor" stroke-width="2" stroke-linejoin="round"/></svg>
    (555)014-2288
  </p>
</article>

</body>
</html>
```